Packaging Design for Vanta Core

We require an outstanding packaging design for our Vanta Core brand, which offers hydration electrolyte supplements specifically tailored for athletes and sporty individuals.

Benchmark packaging design from liquora competitor attached. The product packaging contains 20 x 20g sticks of the product.

Target Market

Psychographic: Health-conscious, active lifestyle, values quality, functionality and sustainability.

product description 1:
HYDRATION BOOSTER
Refresh, Replenish, Recharge!

product description 2:
PREMIUM ISOTONIC ELECTROLYTE DRINK
Nutritional Expertise Since 1992.

Existing Logo: to add "since 1992"

Appeal to Target Market: Create a design that resonates with both men and women in the 25-55 age group.

Grafik Design: Develop a visually striking design that grabs attention in online retail environments like Brindle.

Visuals: glass of water (or symbolic) and sticks (powder) just like benchmark brand liquora.

Design Elements
Use colours that are inside the Vanta-Core Logo, attached.
Product will be available in 3 flavours. Lemon=yellow, Orange=orange, Black Currant=purple

Typography: Utilize strong, clean, and modern fonts. Ensure readability and create a sense of strength, endurance and reliability.

The product will be available in 3 flavours: Lemon, Orange and Johannisbeere

We look forward to seeing your creative ideas and innovative designs for our Vanta Core brand packaging.

```html
<!DOCTYPE html>
<html lang="en">
<head>
<meta charset="utf-8">
<title>Vanta Core Hydration Booster – Lemon pouch</title>
<link rel="stylesheet" href="https://fonts.googleapis.com/css2?family=Lexend:wght@300;400;700;800&family=Archivo:wght@700;800&display=swap">
<style>
  :root {
    --backdrop: #f7ec6a;
    --magenta: #c41f68;
    --magenta-deep: #a8145a;
    --lemon: #f4e31a;
    --white: #ffffff;
    --pink-soft: #f2a6cf;
    --pink-muted: #e9a0c6;
  }
  html, body {
    margin: 0;
    padding: 0;
    width: 1200px;
    height: 972px;
    overflow: hidden;
    background: var(--backdrop);
  }
  .canvas {
    position: relative;
    width: 1200px;
    height: 972px;
    background: var(--backdrop);
    font-family: "Archivo", sans-serif;
  }
  .pouch {
    position: absolute;
    left: 305px;
    top: 223px;
    width: 574px;
    height: 640px;
    overflow: hidden;
    border-radius: 14px;
  }
  .pouch-shape { position: absolute; inset: 0; }
  .count-tab {
    position: absolute;
    left: 35px;
    top: 0;
    width: 67px;
    height: 91px;
    background: var(--lemon);
    color: var(--magenta);
    text-align: center;
  }
  .count-tab .count-number {
    display: block;
    margin-top: 30px;
    font-size: 34px;
    font-weight: 800;
    line-height: 1;
  }
  .count-tab .count-label {
    display: block;
    font-size: 13px;
    font-weight: 700;
    line-height: 1.2;
  }
  .brand {
    position: absolute;
    left: 62px;
    top: 150px;
    display: flex;
    align-items: center;
    gap: 14px;
    color: var(--white);
    font-family: "Lexend", sans-serif;
    font-weight: 800;
    font-size: 62px;
    line-height: 1;
    letter-spacing: -1px;
    white-space: nowrap;
  }
  .brand-dot {
    width: 46px;
    height: 46px;
    border-radius: 50%;
    background: var(--lemon);
    flex: none;
  }
  .since {
    position: absolute;
    right: 140px;
    top: 228px;
    color: var(--white);
    font-family: "Lexend", sans-serif;
    font-weight: 700;
    font-size: 18px;
    white-space: nowrap;
  }
  .stick-visual {
    position: absolute;
    left: 148px;
    top: 300px;
    width: 262px;
    height: 62px;
    transform: rotate(-15deg);
    background: linear-gradient(90deg, #f7f1f4 0%, #ffffff 75%, #f6ec5c 100%);
    border-radius: 3px;
  }
  .glass-visual {
    position: absolute;
    left: 65px;
    top: 410px;
    width: 154px;
    height: 230px;
    background: linear-gradient(180deg, #e9e9ec 0%, #dcdde0 40%, #f0c23a 55%, #e0dfe3 75%, #ececef 100%);
    border-radius: 6px 6px 2px 2px;
  }
  .claims {
    position: absolute;
    right: 56px;
    top: 380px;
    text-align: right;
    white-space: nowrap;
  }
  .product-name {
    margin: 0;
    color: var(--white);
    font-weight: 800;
    font-size: 40px;
    line-height: 0.92;
    letter-spacing: -0.5px;
  }
  .tagline {
    margin: 8px 0 0;
    color: var(--white);
    font-family: "Lexend", sans-serif;
    font-weight: 400;
    font-size: 16px;
  }
  .descriptor {
    margin: 10px 0 0;
    color: var(--pink-soft);
    font-weight: 800;
    font-size: 22px;
    line-height: 1.05;
  }
  .heritage {
    margin: 6px 0 0;
    color: var(--pink-muted);
    font-family: "Lexend", sans-serif;
    font-weight: 300;
    font-size: 12px;
  }
  .flavour {
    position: absolute;
    left: 230px;
    top: 591px;
    color: var(--magenta);
    font-weight: 800;
    font-size: 23px;
    line-height: 1;
    white-space: nowrap;
  }
  .net-content {
    position: absolute;
    right: 56px;
    top: 594px;
    color: var(--magenta);
    font-family: "Lexend", sans-serif;
    font-weight: 400;
    font-size: 15px;
    line-height: 1;
    white-space: nowrap;
  }
</style>
</head>
<body>
<main class="canvas">
  <section class="pouch" aria-label="Vanta Core Hydration Booster pouch, lemon flavour">
    <svg class="pouch-shape" width="574" height="640" viewBox="0 0 574 640" aria-hidden="true">
      <defs>
        <linearGradient id="pouchGloss" x1="0" y1="0" x2="1" y2="0.4">
          <stop offset="0" stop-color="#b8185f"/>
          <stop offset="0.6" stop-color="#cc2a72"/>
          <stop offset="1" stop-color="#c41f68"/>
        </linearGradient>
      </defs>
      <rect width="574" height="640" fill="url(#pouchGloss)"/>
      <line x1="0" y1="60" x2="574" y2="60" stroke="#a8145a" stroke-width="1.5" stroke-dasharray="3 6"/>
      <polygon points="0,548 574,590 574,640 0,640" fill="#f4e31a"/>
    </svg>

    <div class="count-tab">
      <span class="count-number">20</span>
      <span class="count-label">STICKS</span>
    </div>

    <div class="brand">
      <span class="brand-dot"></span>
      <span class="brand-name">Vanta Core</span>
    </div>
    <div class="since">since 1992</div>

    <div class="stick-visual" role="img" aria-label="Single lemon stick sachet pouring powder"></div>
    <div class="glass-visual" role="img" aria-label="Glass of sparkling water with a lemon slice"></div>

    <div class="claims">
      <h1 class="product-name">HYDRATION<br>BOOSTER</h1>
      <p class="tagline">Refresh, Replenish, Recharge!</p>
      <p class="descriptor">PREMIUM ISOTONIC<br>ELECTROLYTE DRINK</p>
      <p class="heritage">Nutritional Expertise Since 1992</p>
    </div>

    <div class="flavour">LEMON</div>
    <div class="net-content">20 x 20g sticks</div>
  </section>
</main>
</body>
</html>
```